Business card design for Automotive workshop

We need a business card for a new automotive repair and tyre shop called Ridgeback Prime Automotive located in New Zealand. We are a clean, modern and fresh workshop and company.

Front needs to feature logo,
my name:
Lachie Westergaard (director)

Address:
48 Marlow Lane
Kereru Bay 3621

Phone: 07 842 1937
Mobile: 027 519 2764
Email: office@ridgebackmotors.co.nz
Website: ridgebackmotors.co.nz

Back needs to feature an area to write down appointment details, date and time.

Also feature a list of jobs and work we do such as,
Vehicle Servicing
All Mechanical Repairs
Warrant of Fitness
Tyres & Wheel Alignments
Automotive Diagnostics
Automotive Parts & Supplies

```html
<!DOCTYPE html>
<html lang="en">
<head>
<meta charset="utf-8">
<title>Ridgeback Prime Automotive – Business Card</title>
<link href="https://fonts.googleapis.com/css2?family=Roboto:wght@300;400;500;700&display=swap" rel="stylesheet">
<style>
  :root {
    --backdrop: #3a322d;
    --card: #2b2b2c;
    --ink: #f2f2f2;
    --ink-soft: #cfcfcf;
    --accent: #e0232b;
    --emboss: #4a4a4c;
  }
  * { box-sizing: border-box; margin: 0; padding: 0; }
  html, body { width: 1200px; height: 847px; overflow: hidden; }
  body {
    background: var(--backdrop);
    font-family: "Roboto", Arial, sans-serif;
    color: var(--ink);
    position: relative;
  }
  .card {
    position: absolute;
    width: 540px;
    height: 309px;
    background: var(--card);
    box-shadow: 0 10px 28px rgba(0,0,0,.45);
    overflow: hidden;
  }
  .card-back { left: 40px; top: 110px; }
  .card-front { left: 620px; top: 420px; }

  /* Back side */
  .back-brand {
    position: absolute; left: 0; right: 0; top: 30px;
    text-align: center;
    font-size: 27px; font-weight: 700; letter-spacing: 1px;
    text-transform: uppercase;
    color: var(--emboss);
  }
  .services {
    position: absolute; left: 0; right: 0; top: 82px;
    text-align: center;
    font-size: 12.5px; line-height: 19px; color: var(--ink-soft);
  }
  .services .dot { color: var(--accent); margin: 0 4px; }
  .appointment-title {
    position: absolute; left: 0; right: 0; top: 138px;
    text-align: center;
    color: var(--accent); font-size: 17px; font-weight: 500; letter-spacing: .5px;
  }
  .field-row {
    position: absolute; left: 40px; right: 40px; top: 180px;
    display: flex; gap: 18px; font-size: 13px; color: var(--ink-soft);
  }
  .field { flex: 1; display: flex; align-items: flex-end; gap: 6px; }
  .field .line { flex: 1; border-bottom: 1px solid var(--ink-soft); height: 14px; }
  .days {
    position: absolute; left: 40px; right: 40px; top: 236px;
    display: flex; justify-content: space-between;
    list-style: none; font-size: 14px; color: var(--ink-soft);
  }
  .days li { display: flex; align-items: center; gap: 7px; }
  .days li::before {
    content: ""; width: 12px; height: 12px;
    border: 1.3px solid var(--accent); border-radius: 50%;
  }

  /* Front side */
  .front-brand {
    position: absolute; right: 34px; top: 46px;
    text-align: right;
    font-size: 28px; font-weight: 700; letter-spacing: 1px;
    text-transform: uppercase; line-height: 1.15;
    color: var(--accent);
  }
  .person {
    position: absolute; left: 24px; top: 178px; width: 240px;
    text-align: right;
  }
  .person-name { color: var(--accent); font-size: 19px; font-weight: 700; text-transform: uppercase; white-space: nowrap; }
  .person-role { font-size: 14px; font-weight: 300; margin-top: 2px; }
  .person-address { font-size: 14px; font-weight: 300; margin-top: 14px; line-height: 1.35; white-space: nowrap; }
  .divider {
    position: absolute; left: 280px; top: 180px;
    width: 1px; height: 92px; background: var(--accent);
  }
  .contacts {
    position: absolute; left: 294px; top: 180px;
    list-style: none; font-size: 14px; font-weight: 300; line-height: 23px;
  }
  .contacts li { display: flex; align-items: center; gap: 7px; white-space: nowrap; }
  .contacts svg { width: 12px; height: 12px; fill: var(--accent); flex: none; }
</style>
</head>
<body>

<section class="card card-back" aria-label="Card back – appointment">
  <div class="back-brand">Ridgeback Prime Automotive</div>
  <p class="services">
    Vehicle Servicing<span class="dot">•</span>All Mechanical Repairs<span class="dot">•</span>Warrant of Fitness<br>
    Tyres &amp; Wheel Alignments<span class="dot">•</span>Automotive Diagnostics<span class="dot">•</span>Automotive Parts &amp; Supplies
  </p>
  <h2 class="appointment-title">APPOINTMENT</h2>
  <div class="field-row">
    <div class="field">Date:<span class="line"></span></div>
    <div class="field">Time:<span class="line"></span></div>
  </div>
  <ul class="days">
    <li>Mon</li><li>Tue</li><li>Wed</li><li>Thu</li><li>Fri</li>
  </ul>
</section>

<section class="card card-front" aria-label="Card front – contact">
  <div class="front-brand">Ridgeback Prime<br>Automotive</div>

  <div class="person">
    <div class="person-name">Lachie Westergaard</div>
    <div class="person-role">director</div>
    <div class="person-address">48 Marlow Lane, Kereru Bay 3621</div>
  </div>

  <div class="divider"></div>

  <ul class="contacts">
    <li><svg viewBox="0 0 24 24"><path d="M6.6 10.8a15.1 15.1 0 0 0 6.6 6.6l2.2-2.2c.3-.3.7-.4 1-.2 1.1.4 2.3.6 3.6.6.6 0 1 .4 1 1V20c0 .6-.4 1-1 1A17 17 0 0 1 3 4c0-.6.4-1 1-1h3.5c.6 0 1 .4 1 1 0 1.3.2 2.5.6 3.6.1.3 0 .7-.2 1z"/></svg>07 842 1937</li>
    <li><svg viewBox="0 0 24 24"><path d="M7 1h10a2 2 0 0 1 2 2v18a2 2 0 0 1-2 2H7a2 2 0 0 1-2-2V3a2 2 0 0 1 2-2zm0 3v14h10V4zm5 15.5a1 1 0 1 0 0 2 1 1 0 0 0 0-2z"/></svg>027 519 2764</li>
    <li><svg viewBox="0 0 24 24"><path d="M2 5h20v14H2zm2 2v.5l8 5 8-5V7zm0 3v7h16v-7l-8 5z"/></svg>office@ridgebackmotors.co.nz</li>
    <li><svg viewBox="0 0 24 24"><path d="M12 2a10 10 0 1 0 0 20 10 10 0 0 0 0-20zm0 2c1 0 2.3 2.2 2.7 6H9.3C9.7 6.2 11 4 12 4zm-7.9 6a8 8 0 0 1 4.6-5.3A15 15 0 0 0 7.3 10zm0 4h3.2c.2 1.9.7 3.8 1.4 5.3A8 8 0 0 1 4.1 14zm5.2 0h5.4c-.4 3.8-1.7 6-2.7 6s-2.3-2.2-2.7-6zm7.4 0h3.2a8 8 0 0 1-4.6 5.3c.7-1.5 1.2-3.4 1.4-5.3zm0-4a15 15 0 0 0-1.4-5.3 8 8 0 0 1 4.6 5.3z"/></svg>ridgebackmotors.co.nz</li>
  </ul>
</section>

</body>
</html>
```